Business Card Design

I have a very clear idea of what I want. I just do not know how to do the graphic design to match it.

On the front I want the uploaded image with the horse and the two people.
I want

Bottom left hand corner
Lenny Firth
0472 316 508

Bottom right
There is maroon block with Morris Tane Practitioner Group Logo
Next to that I want the Stable Arc tile about the same size ( attached psd file)

On the back I want a plain colour (white) with the information

Lenny Firth
Equine Performance
Brindle4Ponies and Acupuncture
Horsemanship Lessons and Clinics
Horse Training

lfirth@critterloop.com.au
FB/lenny.firth.263
StableArc.com.au

Lenny Firth
0472 316 508
lfirth@critterloop.com.au

```html
<!DOCTYPE html>
<html lang="en">
<head>
<meta charset="utf-8">
<title>Lenny Firth – Business Card</title>
<link rel="stylesheet" href="https://fonts.googleapis.com/css2?family=Lora:ital,wght@0,400;0,600;1,400;1,600&family=Open+Sans:wght@600;700&family=Playball&display=swap">
<style>
  :root {
    --navy: #1f3e73;
    --navy-dark: #173260;
    --sand-light: #e3cf9f;
    --sand-mid: #cfb27a;
    --sand-dark: #b08d57;
    --brown-script: #5a3a24;
    --maroon: #6e2a1a;
    --cream: #f1e6cf;
    --white: #ffffff;
    --stage: #ecebe8;
    --tile-edge: #7a4a2a;
  }
  * { box-sizing: border-box; margin: 0; padding: 0; }
  html, body { width: 1200px; height: 950px; overflow: hidden; }
  body {
    background: var(--stage);
    position: relative;
    font-family: "Lora", Georgia, serif;
  }
  .card {
    position: absolute;
    left: 240px;
    width: 720px;
    height: 411px;
    overflow: hidden;
    box-shadow: 0 6px 18px rgba(0,0,0,0.18);
  }
  .card--front { top: 42px; }
  .card--back { top: 497px; background: var(--white); }

  /* Front */
  .front-photo {
    position: absolute;
    inset: 0 0 84px 0;
    background: radial-gradient(ellipse at 65% 45%, var(--sand-light) 0%, var(--sand-mid) 60%, var(--sand-dark) 100%);
  }
  .tagline {
    position: absolute;
    left: 44px;
    top: 120px;
    color: var(--brown-script);
  }
  .tagline__lead {
    font-family: "Lora", Georgia, serif;
    font-size: 17px;
    letter-spacing: 3px;
    text-transform: uppercase;
    margin-left: 6px;
  }
  .tagline__your {
    font-family: "Playball", cursive;
    font-size: 30px;
    margin-left: 170px;
    margin-top: -2px;
    display: block;
  }
  .tagline__main {
    font-family: "Playball", cursive;
    font-size: 92px;
    line-height: 0.9;
    display: block;
    margin-top: -14px;
  }
  .front-band {
    position: absolute;
    left: 0; right: 0; bottom: 0;
    height: 84px;
    background: linear-gradient(180deg, var(--navy) 0%, var(--navy-dark) 100%);
    color: var(--white);
    font-family: "Open Sans", Arial, sans-serif;
    padding: 12px 0 0 36px;
  }
  .front-band__name { font-size: 26px; font-weight: 700; letter-spacing: 1px; line-height: 1.15; }
  .front-band__phone { font-size: 28px; font-weight: 600; letter-spacing: 2px; line-height: 1.15; }

  .partner-block {
    position: absolute;
    right: 128px;
    bottom: 110px;
    width: 96px;
    height: 84px;
    background: var(--maroon);
    color: var(--cream);
    font-family: "Lora", Georgia, serif;
    font-size: 12px;
    line-height: 1.25;
    text-align: center;
    display: flex;
    align-items: center;
    justify-content: center;
    padding: 8px;
  }
  .brand-tile {
    background: var(--white);
    border: 4px solid var(--tile-edge);
    border-radius: 14px;
    display: flex;
    align-items: center;
    justify-content: center;
    color: var(--navy);
    font-family: "Lora", Georgia, serif;
    font-weight: 600;
    text-align: center;
    box-shadow: 0 3px 0 var(--tile-edge), 0 6px 8px rgba(0,0,0,0.25);
  }
  .brand-tile--small {
    position: absolute;
    right: 36px;
    bottom: 114px;
    width: 76px;
    height: 76px;
    font-size: 14px;
  }

  /* Back */
  .back-panel {
    position: absolute;
    left: 0; top: 0; bottom: 0;
    width: 420px;
    background: var(--navy);
    color: var(--white);
    padding: 40px 0 0 40px;
    font-style: italic;
  }
  .back-panel__name {
    font-family: "Open Sans", Arial, sans-serif;
    font-style: normal;
    font-weight: 700;
    font-size: 24px;
    margin-bottom: 8px;
  }
  .services { list-style: none; font-size: 17px; line-height: 1.5; margin-bottom: 22px; }
  .contacts { list-style: none; font-size: 16px; line-height: 1.55; }
  .brand-tile--large {
    position: absolute;
    left: 500px;
    top: 120px;
    width: 150px;
    height: 150px;
    font-size: 26px;
  }
</style>
</head>
<body>
  <section class="card card--front" aria-label="Business card front">
    <div class="front-photo" role="img" aria-label="Overhead photo of a horse and two people on a sandy arena"></div>
    <div class="tagline">
      <span class="tagline__lead">How you ever gonna know</span>
      <span class="tagline__your">Your</span>
      <span class="tagline__main">Potential</span>
    </div>
    <div class="partner-block">Morris Tane Practitioner Group</div>
    <div class="brand-tile brand-tile--small">Stable Arc</div>
    <div class="front-band">
      <p class="front-band__name">Lenny Firth</p>
      <p class="front-band__phone">0472 316 508</p>
    </div>
  </section>

  <section class="card card--back" aria-label="Business card back">
    <div class="back-panel">
      <p class="back-panel__name">Lenny Firth</p>
      <ul class="services">
        <li>Equine Performance</li>
        <li>Brindle4Ponies &amp; Acupuncture</li>
        <li>Horsemanship Lessons &amp; Clinics</li>
        <li>Horse Training</li>
      </ul>
      <ul class="contacts">
        <li>lfirth@critterloop.com.au</li>
        <li>StableArc.com.au</li>
        <li>FB/lenny.firth.263</li>
      </ul>
    </div>
    <div class="brand-tile brand-tile--large">Stable Arc</div>
  </section>
</body>
</html>
```